Greyfield Ridge Medical Website to make connecting and communicating easier

To create a unique, user-friendly, professional website for patients and professionals to access education/ information, forms, appointments, contact details, and data about us, and for us to have the capacity to link to various cloud-based platforms.
To use the logo design and colour scheme we have just sourced.

WEBSITE to be eye catching, Inspiring and alluring
- efficient and logical
- professional and trustworthy appearance
- health focus "living health matters"
- user friendly
- ability to link with cloud-based software and video conferencing tools/ telehealth
- colours- black/ white teal and ?silver

PAGES:
page 1 - Our clinic and staff, services offered, contact us- address/ map / contact details- social media connections
page 2- patients and visitors - New patient forms to complete, news and patient informtion (educatinal)
page 3 - health professionals -referral forms, research and education
page 3- online appointments
page 4 - Quick links - partners, other services
page 5- privacy policy, disclaimer

HI, Could we please extend the deadline another 5 days, so sorry just struggling with my workload to be able to keep up and I am wanting to liaise more with the designer that I will choose. I am so happy with PixelHarbor and all the designers - thank you! Thank you so much!!

Target Market(s)

Patients - mostly over 60's so the website must be minimal clicks and simple to navigate
Professionals - for education and access forms

Industry/Entity Type

Health Care

Coding

Coded - Design and coding required

Number of Pages Required

5+ page

Font styles to use
Sans Serif
Script

Colors
33b8a4
86cfc6

Requirements
Must have
• WEBSITE to be eye catching, Inspiring and alluring
- efficient and logical
- user friendly

WEBSITE - professional and user friendly
- ability to link with cloud based software and videoconferencing/ telehealth
Nice to have
• clean and crisp presentation
happy for an innovative look
room to add more services and ability to link pages and resources
Should not have
• Please ensure the website is not:
clunky
difficult to navigate
common and cheap looking

```html
<!DOCTYPE html>
<html lang="en">
<head>
<meta charset="utf-8">
<title>Privacy Policy – Greyfield Ridge Medical</title>
<link rel="stylesheet" href="https://fonts.googleapis.com/css2?family=Roboto:wght@400;500;700&display=swap">
<style>
:root{
  --teal:#33b8a4;
  --teal-soft:#86cfc6;
  --mint:#baf3ee;
  --ink:#222;
  --body:#555;
  --white:#fff;
}
*{margin:0;padding:0;box-sizing:border-box}
html,body{width:1200px;height:2811px;overflow:hidden}
body{font-family:"Roboto",Arial,sans-serif;color:var(--ink);background:var(--white);position:relative}
.site-header{position:absolute;top:0;left:0;width:1200px;height:77px;background:var(--white)}
.brand{position:absolute;left:93px;top:26px;display:flex;align-items:center;gap:8px;color:var(--teal);font-size:15px;font-weight:500;width:120px;line-height:1.15}
.brand-dot{width:14px;height:14px;border-radius:50%;background:var(--teal);flex:none}
.main-nav a{position:absolute;top:34px;font-size:12px;color:var(--ink);text-decoration:none}
.main-nav a.active{color:var(--teal)}
.contact-btn{position:absolute;left:1006px;top:22px;width:105px;height:37px;border-radius:3px;background:var(--teal);color:var(--white);font-size:12px;display:flex;align-items:center;justify-content:center}
.hero{position:absolute;top:77px;left:0;width:1200px;height:375px;background:linear-gradient(120deg,#8a8f93 0%,#6f7478 45%,#4a5058 75%,#3d4450 100%)}
.hero-title{position:absolute;top:153px;width:100%;text-align:center;color:var(--white);font-size:29px;font-weight:400}
.breadcrumb{position:absolute;top:198px;width:100%;text-align:center;color:var(--white);font-size:12px}
.breadcrumb span{margin:0 9px}
.policy{position:absolute;top:452px;left:84px;width:776px;height:1950px;overflow:hidden}
.policy h2{font-size:29px;font-weight:500;color:var(--ink);line-height:1.2}
.policy p{font-size:12px;line-height:20px;color:var(--body)}
.policy p b{color:#333;font-weight:700}
.gap-s{margin-top:8px}
.gap-p{margin-top:20px}
.footer{position:absolute;top:2402px;left:0;width:1200px;height:346px;background:var(--mint)}
.footer-col{position:absolute;top:70px}
.footer-col h3{font-size:20px;font-weight:400;color:var(--ink);margin-bottom:14px}
.footer-col li{list-style:none;font-size:12px;line-height:24px;color:#444}
.footer-col p{font-size:12px;line-height:20px;color:#444;width:205px;margin-bottom:6px}
.contact-line{display:flex;align-items:center;gap:10px;font-size:12px;line-height:22px;color:#444}
.socials{display:flex;gap:26px;margin-top:20px}
.socials span{width:14px;height:14px;border-radius:50%;background:var(--ink);display:block}
.copyright{position:absolute;top:2748px;left:0;width:1200px;height:63px;background:var(--teal);color:var(--white);font-size:12px;display:flex;align-items:center;justify-content:center}
</style>
</head>
<body>
<header class="site-header">
  <div class="brand"><span class="brand-dot"></span>Greyfield Ridge Medical</div>
  <nav class="main-nav">
    <a style="left:371px">Home</a>
    <a style="left:442px">Services</a>
    <a style="left:526px">Our Doctors</a>
    <a class="active" style="left:631px">Appoinments</a>
    <a style="left:738px">Patients &amp; visitors</a>
  </nav>
  <div class="contact-btn">Contacts Us</div>
</header>

<section class="hero" role="img" aria-label="Dentist treating a patient in a dental chair, darkened backdrop">
  <h1 class="hero-title">Privacy Policy,</h1>
  <div class="breadcrumb"><span>Home</span><span>Privacy Policy,</span></div>
</section>

<main class="policy">
  <h2 style="margin-top:68px">Privacy statement</h2>
  <p style="margin-top:16px">These notices describe how medical information about you may be used and disclosed and how you can get access to this information. PLEASE REVIEW YOUR STATE'S NOTICE CAREFULLY. Our staff are committed to protecting your health information, which is a right you have and one detailed in the federal Health Insurance Portability and Accountability Act (HIPAA) of 1996.</p>

  <h2 style="margin-top:44px">Non-Discrimination and Access to Healthcare</h2>
  <p style="margin-top:16px">Greyfield Ridge does not exclude, deny benefits to, or otherwise discriminate against any person on the basis or race; color; religion; national origin; culture; language; physical or mental disability; genetic information; age; sex, including pregnancy, childbirth or related medical conditions; marital status; sexual orientation; gender identity or expression; socioeconomic status; or source of payment in admission to, participation in, or receipt of the services and benefits of any of its programs and activities, whether carried out by Greyfield Ridge directly or through a contractor or other entity with whom Greyfield Ridge arranges to carry out its programs and activities. Free foreign language interpreters are available for individuals who are limited English proficient. Free sign language and oral interpreters, TTY's and other services are available to deaf and hard-of-hearing persons. For further information about this policy, contact: Greyfield Ridge Director of Internal Audit &amp; Compliance, 1-700-000-000 or TDD 1-700-000-000</p>

  <h2 style="margin-top:26px">Web privacy policy</h2>
  <p class="gap-s">We take your privacy seriously, and we want you to know how we collect, use, share and protect your information. In addition to this privacy policy, users of our Clinic site should consult our Clinic site terms of use as well as any product specific terms and conditions that apply. You may review policies specifically related to patient information (protected health information, or PHI) submitted through our Clinic's patient portal. This policy applies to GreyfieldRidge.org, Greyfield Ridge .edu and other Web locations under our Clinic's control. Other Greyfield Ridge Clinic online properties may have their own privacy policies that apply to those sites. You should review those privacy policies in connection with your use of those sites.</p>

  <h2 style="margin-top:26px">What information we collect</h2>
  <p class="gap-s"><b>Information you give us:</b> We respect the right to privacy of all visitors to the Greyfield Ridge Clinic sites. We receive and store information you enter on our sites or give us in any other way, such as name, email address and phone number. This includes information you submit on forms, such as appointment request forms. Some forms collect sensitive information, such as health information, necessary for us to provide our services to you.</p>
  <p class="gap-p"><b>Information we collect automatically:</b> When you interact with our sites, certain information about your use of our sites is automatically collected. This information includes computer and connection information, such as statistics on your page views, traffic to and from our sites, referral URL, ad data, your IP address, and device identifiers. This information also may include your transaction history, and your web log information, how you search for our sites, the websites you click on from our sites or emails, whether and when you open our emails, and your browsing activities across other websites.</p>
  <p class="gap-p">Much of this information is collected through cookies, web beacons and other tracking technologies, as well as through your web browser or device (e.g., IP address, MAC address, browser version, etc.).</p>

  <h2 style="margin-top:26px">Other Infos</h2>
  <p class="gap-s">Lorem ipsum dolor sit amet, consectetur adipiscing elit. Morbi porta orci quis volutpat imperdiet. Nunc ligula eros, fermentum in arcu at, tristique rutrum elit. Nullam fermentum ligula non est malesuada rutrum. Morbi mollis vitae leo et fermentum. Etiam vitae viverra leo, condimentum porttitor nulla. Donec at felis malesuada, vehicula metus at, blandit ante. Donec at tellus at augue tincidunt cursus ac sit amet quam. Donec congue blandit vestibulum.Lorem ipsum dolor sit amet, consectetur adipiscing elit. Morbi porta orci quis volutpat imperdiet. Nunc ligula eros, fermentum in arcu at, tristique rutrum elit. Nullam fermentum ligula non est malesuada rutrum. Morbi mollis vitae leo et fermentum. Etiam vitae viverra leo, condimentum porttitor nulla. Donec at felis malesuada, vehicula metus at, blandit ante. Donec at tellus at augue tincidunt cursus ac sit amet quam. Donec congue blandit vestibulum.Lorem ipsum dolor sit amet, consectetur adipiscing elit. Morbi porta orci quis volutpat imperdiet. Nunc ligula eros, fermentum in arcu at, tristique rutrum elit. Nullam fermentum ligula non est malesuada rutrum. Morbi mollis vitae leo et fermentum. Etiam vitae viverra leo, condimentum porttitor nulla. Donec at felis malesuada, vehicula metus at, blandit ante. Donec at tellus at augue tincidunt cursus ac sit amet quam. Donec congue blandit vestibulum.Lorem ipsum dolor sit amet, consectetur adipiscing elit. Morbi porta orci quis volutpat imperdiet. Nunc ligula eros, fermentum in arcu at, tristique rutrum elit. Nullam fermentum ligula non est malesuada rutrum. Morbi mollis vitae leo et fermentum. Etiam vitae viverra leo, condimentum porttitor nulla. Donec at felis malesuada, vehicula metus at, blandit ante. Donec at tellus at augue tincidunt cursus ac sit amet quam. Donec congue blandit vestibulum.Lorem ipsum dolor sit amet, consectetur adipiscing elit. Morbi porta orci quis volutpat imperdiet. Nunc ligula eros, fermentum in arcu at, tristique rutrum elit. Nullam fermentum ligula non est malesuada rutrum. Morbi mollis vitae leo et fermentum. Etiam vitae viverra leo, condimentum porttitor nulla. Donec at felis malesuada, vehicula metus at, blandit ante. Donec at tellus at augue tincidunt cursus ac sit amet quam. Donec congue blandit vestibulum.Lorem ipsum dolor sit amet, consectetur adipiscing elit. Morbi porta orci quis volutpat imperdiet. Nunc ligula eros, fermentum in arcu at, tristique rutrum elit. Nullam fermentum ligula non est malesuada rutrum. Morbi mollis vitae leo et fermentum. Etiam vitae viverra leo, condimentum porttitor nulla. Donec at felis malesuada, vehicula metus at, blandit ante. Donec at tellus at augue tincidunt cursus ac sit amet quam. Donec congue blandit vestibulum.</p>

  <h2 style="margin-top:38px">Lorem ipsum</h2>
  <p class="gap-s">Lorem ipsum dolor sit amet, consectetur adipiscing elit. Morbi porta orci quis volutpat imperdiet. Nunc ligula eros, fermentum in arcu at, tristique rutrum elit. Nullam fermentum ligula non est malesuada rutrum. Morbi mollis vitae leo et fermentum. Etiam vitae viverra leo, condimentum porttitor nulla. Donec at felis malesuada, vehicula metus at, blandit ante. Donec at tellus at augue tincidunt cursus ac sit amet quam. Donec congue blandit vestibulum.Lorem ipsum dolor sit amet, consectetur adipiscing elit. Morbi porta orci quis volutpat imperdiet. Nunc ligula eros, fermentum in arcu at, tristique rutrum elit. Nullam fermentum ligula non est malesuada rutrum. Morbi mollis vitae leo et</p>

  <h2 style="margin-top:26px">Lorem&nbsp; sit amet</h2>
  <p class="gap-s">Lorem ipsum dolor sit amet, consectetur adipiscing elit. Morbi porta orci quis volutpat imperdiet. Nunc ligula eros, fermentum in arcu at, tristique rutrum elit. Nullam fermentum ligula non est malesuada rutrum. Morbi mollis vitae leo et fermentum. Etiam vitae viverra leo, condimentum porttitor nulla. Donec at felis malesuada, vehicula metus at, blandit ante. Donec at tellus at augue tincidunt cursus ac sit amet quam. Donec congue blandit vestibulum.Lorem ipsum dolor sit amet, consectetur adipiscing elit. Morbi porta orci quis volutpat imperdiet. Nunc ligula eros, fermentum in arcu at, tristique rutrum elit. Nullam fermentum ligula non est malesuada rutrum. Morbi mollis vitae leo et</p>

  <h2 style="margin-top:26px">Ipsum dolor sit amet</h2>
  <p class="gap-s">Lorem ipsum dolor sit amet, consectetur adipiscing elit. Morbi porta orci quis volutpat imperdiet. Nunc ligula eros, fermentum in arcu at, tristique rutrum elit. Nullam fermentum ligula non est malesuada rutrum. Morbi mollis vitae leo et fermentum. Etiam vitae viverra leo, condimentum porttitor nulla. Donec at felis malesuada, vehicula metus at, blandit ante. Donec at tellus at augue tincidunt cursus ac sit amet quam. Donec congue blandit vestibulum.Lorem ipsum dolor sit amet, consectetur adipiscing elit. Morbi porta orci quis volutpat imperdiet. Nunc ligula eros, fermentum in arcu at, tristique rutrum elit. Nullam fermentum ligula non est malesuada rutrum. Morbi mollis vitae leo et</p>
</main>

<footer class="footer">
  <div class="footer-col" style="left:97px">
    <h3>Contact Us</h3>
    <p>Lorem ipsum dolor sit amet, consectetur adipiscing elit, sed do eiusmod tempor incididunt</p>
    <div class="contact-line">
      <svg width="12" height="14" viewBox="0 0 12 14"><path d="M6 0a5 5 0 0 0-5 5c0 4 5 9 5 9s5-5 5-9a5 5 0 0 0-5-5zm0 7a2 2 0 1 1 0-4 2 2 0 0 1 0 4z" fill="#222"/></svg>
      42 Linden Way CA, USA</div>
    <div class="contact-line">
      <svg width="12" height="12" viewBox="0 0 12 12"><path d="M2.5 0.5l2 2.5-1.2 1.5c.8 1.7 2.2 3.1 3.9 3.9L8.7 7l2.8 2-.8 2.2C5.5 11.2.8 6.5.5 1.3z" fill="#222"/></svg>
      +1-555-784-444</div>
    <div class="contact-line">
      <svg width="12" height="10" viewBox="0 0 12 10"><rect x=".5" y=".5" width="11" height="9" fill="none" stroke="#222"/><path d="M.5.5 6 5.5 11.5.5" fill="none" stroke="#222"/></svg>
      hello@greyfield.example</div>
  </div>
  <div class="footer-col" style="left:399px">
    <h3>Quick Links</h3>
    <ul><li>General information</li><li>Emergency service</li><li>Ambulance</li><li>Medical research</li><li>Blood bank</li><li>Intensive care service</li></ul>
  </div>
  <div class="footer-col" style="left:611px">
    <h3>Join Our Community</h3>
    <ul><li>Blog postes</li><li>Join our forum</li><li>Meet our doctors</li><li>Medical research</li><li>Help center</li><li>Contract us</li></ul>
  </div>
  <div class="footer-col" style="left:913px">
    <h3>Open Time</h3>
    <ul><li>Mon-Fri 8:00 AM - 10:00 PM</li><li>Sat-Sun 9:00 AM - 6:00 PM</li><li>Emergency 24/24 hours</li></ul>
    <div class="socials" aria-label="Social media links"><span></span><span></span><span></span><span></span></div>
  </div>
</footer>
<div class="copyright">Copyright 2020 . All rights reserved &nbsp; Greyfield Ridge</div>
</body>
</html>
```